Business Card Design for a Personal Trainer

I need a business card design for my job as a personal trainer. It should have a unique, modern and exclusive design. On the front there should be only my logo with my name and my job. 0163/2918374 Tobias Kellinger Lindenfeldweg 14 80412 Munich Germany The most important contact information is the web adress. it can be bigger than the rest, but its not necessary. The card should be 8,5cmx5,5cm big. Font: Roboto. Colors: black, white, gray, 56c1ff.

```html
<!DOCTYPE html>
<html lang="de">
<head>
<meta charset="utf-8">
<title>Tobias Kellinger – Personal Trainer Business Card</title>
<link rel="stylesheet" href="https://fonts.googleapis.com/css2?family=Roboto:wght@300;400;500&display=swap">
<style>
  :root {
    --backdrop: #3a3a3a;
    --card-light: #ececec;
    --ink: #111111;
    --white: #ffffff;
    --accent: #56c1ff;
    --scene-top: #2c2b38;
    --scene-mid: #55546a;
    --scene-low: #1f1f29;
    --band: rgba(150, 150, 165, 0.35);
    --portrait-a: #5a5a5a;
    --portrait-b: #2a2a2a;
  }
  * { margin: 0; padding: 0; box-sizing: border-box; }
  html, body {
    width: 1200px; height: 1200px; overflow: hidden;
    background: var(--backdrop);
    font-family: "Roboto", Arial, sans-serif;
  }
  .card {
    position: absolute; left: 246px; width: 708px;
    border-radius: 18px; overflow: hidden;
  }
  .brand-mark {
    display: block; margin: 0 auto; background: var(--accent);
  }
  /* Front */
  .card-front { top: 152px; height: 401px; }
  .front-scene {
    position: absolute; inset: 0;
    background: linear-gradient(180deg, var(--scene-top) 0%, var(--scene-mid) 45%, var(--scene-low) 70%, var(--scene-mid) 100%);
  }
  .front-brand {
    position: absolute; left: 0; right: 0; top: 96px;
    text-align: center; color: var(--white);
  }
  .front-brand .brand-mark { width: 64px; height: 64px; margin-bottom: 26px; }
  .brand-name {
    font-weight: 400; font-size: 31px; letter-spacing: 0.5px; line-height: 1;
  }
  .brand-role {
    display: flex; align-items: center; justify-content: center; gap: 8px;
    font-size: 13px; letter-spacing: 3.5px; margin-top: 6px; line-height: 1;
  }
  .brand-role::before, .brand-role::after {
    content: ""; height: 1.5px; width: 48px; background: currentColor;
  }
  .web-band {
    position: absolute; left: 0; right: 0; bottom: 0; height: 93px;
    background: var(--band);
    display: flex; align-items: center; justify-content: center;
    color: var(--white); font-size: 34px; font-weight: 400;
  }
  /* Back */
  .card-back { top: 625px; height: 403px; background: var(--card-light); }
  .portrait {
    position: absolute; left: 52px; top: 51px; width: 266px; height: 352px;
    border-radius: 133px 133px 0 0;
    background: radial-gradient(ellipse at 50% 35%, var(--portrait-a) 0%, var(--portrait-b) 80%);
  }
  .divider {
    position: absolute; left: 366px; top: 67px; width: 3px; height: 271px;
    background: var(--ink);
  }
  .back-brand {
    position: absolute; left: 370px; width: 330px; top: 76px;
    text-align: center; color: var(--ink);
  }
  .back-brand .brand-mark { width: 54px; height: 54px; margin-bottom: 20px; }
  .back-brand .brand-name { font-size: 26px; }
  .back-brand .brand-role { font-size: 10px; letter-spacing: 2.6px; margin-top: 3px; }
  .back-brand .brand-role::before, .back-brand .brand-role::after { width: 36px; }
  .contact-name {
    position: absolute; left: 414px; top: 209px;
    font-size: 22px; color: var(--ink);
  }
  .contact-list {
    position: absolute; left: 412px; top: 261px; list-style: none;
    font-size: 18px; color: var(--ink); line-height: 24px;
  }
  .contact-list li { display: flex; align-items: flex-start; }
  .contact-list svg { width: 16px; height: 16px; margin: 4px 14px 0 0; flex: none; fill: var(--ink); }
</style>
</head>
<body>
  <section class="card card-front">
    <div class="front-scene" role="img" aria-label="Photo of an athlete standing on a wet beach under a dark cloudy sky"></div>
    <div class="front-brand">
      <span class="brand-mark"></span>
      <div class="brand-name">TOBIAS KELLINGER</div>
      <div class="brand-role">PERSONAL TRAINER</div>
    </div>
    <div class="web-band">www.tobiaskellinger.de</div>
  </section>

  <section class="card card-back">
    <div class="portrait" role="img" aria-label="Black and white portrait of the trainer with arms crossed"></div>
    <div class="divider"></div>
    <div class="back-brand">
      <span class="brand-mark"></span>
      <div class="brand-name">TOBIAS KELLINGER</div>
      <div class="brand-role">PERSONAL TRAINER</div>
    </div>
    <div class="contact-name">Tobias Kellinger</div>
    <ul class="contact-list">
      <li>
        <svg viewBox="0 0 16 16" aria-hidden="true"><path d="M1 5c0-2 3-3 7-3s7 1 7 3v1h-3.5V5h-7v1H1z"/><path d="M3 7h10l1 6H2z"/></svg>
        <span>0163/2918374</span>
      </li>
      <li>
        <svg viewBox="0 0 16 16" aria-hidden="true"><path d="M1 6l7-5 7 5v9H1z"/><path d="M3 7l5 4 5-4" fill="none" stroke="#ececec" stroke-width="1.5"/></svg>
        <span>t.kellinger@postfach.de</span>
      </li>
      <li>
        <svg viewBox="0 0 16 16" aria-hidden="true"><path d="M8 1l8 7h-2v7H10v-5H6v5H2V8H0z"/></svg>
        <span>Lindenfeldweg 14<br>80412 München</span>
      </li>
    </ul>
  </section>
</body>
</html>
```